Stationery Design Project

We need a stationery design for our Norwegian trucking company. We have existed for about 15 years and our 12 drivers uses relatively new vehicles to transport goods around in northern Norway. Long distance routes with fresh fish og food transport is our main operations.

We have already made alogo that's printed on our trucks. The logo and a picture of our trucks is attached. I think the logo i crappy, but since its already in use, changing it is not an option in this round. Still using a better colour scheme in the overall stationery and more interesting fonts is possible (altso in the logo).

Company details:
Name: Vikmarka AS
Organisation nr 983 517 608
Post adress: 8640 Brekka

I like minimalism and simplicity. I am avalibly for questions in normal GMT working hours either here or on mail: kjell@brekkafrakt.no

Reason: Hi. Im extending the deadline because I needed some time to find a vector file of our logo. Sorry for the inconvenience

Hi, and thanks for all your interest in the project. Some updates:

-          I have decided to commit to using one of the designs. Some designer will get the payment.

-          I have extended the deadline with 24 hours since I needed some time to find our firms vector logo (a slow Swedish man was holding me up)

-          We will not choose a design before the deadline. No need to rush.

-          We have received a lot of great design and think there is a need to specified the product we want to make:

o   Business Card for all our employers. I just need the design and will duplicate with the correct numbers and name myself. The information on should be: Logo, employer’s name, Phone number, email, website, Postal number and address. Use this as a template: logo, Leif Dahlberg, 47382950, Leif@brekkafrakt.no,, brekkafrakt.no, 8640 Brekka. The order and placement of the information is your creative decision.

o   Stickers to put on the goods we travel. On the sticker the should be the following information: Logo, phone number, Tekst and link: Fraktæ av Vikmarka. Ke du syns? Brekkafrakt.no/tilbakemelding (this means: Handled by Vikmarka. What do you think Brekkafrakt.no/feedback -à the link will be a feedback form). The placement the information and size is your creative decision with some stings: we have been thinking of using Prentolo for printing and see that a size about 6x6 cm, 8x5 or something like that. (with 3000 copies our budget is 200 punds). Any suggestions of other suppliers are welcome. Prentolo price calculator http://www.prentoloprints.example/digital-litho-printing/printing-labels-tags/stickers/

o   Letterhead with logo, address, phone number and organizational number.

o   Envelopes with logo,address, phone number and organizational number.

Have a nice day.

 

 

• Using the blue colour in the logo and using a similar graphic approch.

```html
<!DOCTYPE html>
<html lang="no">
<head>
<meta charset="utf-8">
<title>Vikmarka AS – Stationery</title>
<link href="https://fonts.googleapis.com/css2?family=Tinos:wght@400;700&display=swap" rel="stylesheet">
<style>
  :root {
    --backdrop: #e4e5e6;
    --paper: #ffffff;
    --edge: #d5d8dc;
    --navy: #2b3690;
    --ink-blue: #2c6ea6;
    --band-deep: #135f96;
    --band-mid: #2f89c4;
    --band-light: #9fcfe7;
    --envelope: #b6dcea;
    --ring: #a9d2e4;
  }
  * { margin: 0; padding: 0; box-sizing: border-box; }
  html, body { width: 1200px; height: 900px; overflow: hidden; }
  body {
    position: relative;
    background: var(--backdrop);
    font-family: "Tinos", "Times New Roman", serif;
    font-weight: 700;
    color: var(--navy);
  }
  .piece { position: absolute; overflow: hidden; }
  .band { position: absolute; left: 0; width: 100%; display: block; }

  .brand {
    position: absolute;
    display: flex;
    align-items: center;
    gap: 6px;
    color: var(--navy);
    font-weight: 700;
    white-space: nowrap;
  }
  .brand-dot { border-radius: 50%; background: var(--navy); flex: none; }

  /* Letterhead */
  .letterhead {
    left: 300px; top: 75px; width: 535px; height: 755px;
    background: var(--paper); border: 1px solid var(--edge);
  }
  .letterhead .band { top: 0; height: 120px; }
  .letterhead .brand { left: 74px; top: 16px; font-size: 22px; }
  .letterhead .brand-dot { width: 12px; height: 12px; }
  .letterhead-rule {
    position: absolute; left: 28px; right: 28px; top: 686px;
    height: 2px; background: var(--navy);
  }
  .letterhead-footer {
    position: absolute; left: 0; right: 0; top: 694px;
    text-align: center; color: var(--ink-blue); font-size: 14.5px; line-height: 19px;
  }

  /* Business card */
  .business-card {
    left: 153px; top: 257px; width: 230px; height: 128px;
    background: var(--paper); border: 1px solid var(--edge);
  }
  .business-card .band { bottom: 0; height: 30px; }
  .business-card .brand { left: 12px; top: 9px; font-size: 11px; gap: 4px; }
  .business-card .brand-dot { width: 7px; height: 7px; }
  .card-details {
    position: absolute; right: 32px; top: 34px; text-align: right;
    font-weight: 400; font-size: 8px; line-height: 10px; color: var(--navy);
  }
  .card-name { font-weight: 700; font-size: 11px; line-height: 14px; }

  /* Sticker */
  .sticker {
    left: 221px; top: 453px; width: 194px; height: 194px; border-radius: 50%;
    background: var(--paper); border: 5px solid var(--ring);
  }
  .sticker .band { top: 50px; height: 14px; }
  .sticker .brand { left: 48px; top: 26px; font-size: 12px; gap: 4px; }
  .sticker .brand-dot { width: 7px; height: 7px; }
  .sticker-text {
    position: absolute; left: 0; right: 0; top: 76px; text-align: center;
    font-size: 11.5px; line-height: 16px; color: var(--navy);
  }
  .sticker-text .accent { color: var(--ink-blue); }
  .sticker-text .phone { margin-top: 4px; font-size: 12px; color: var(--ink-blue); }

  /* Envelope */
  .envelope {
    left: 515px; top: 385px; width: 560px; height: 280px;
    background: var(--envelope); border: 1px solid #a8cddc;
  }
  .envelope .band { bottom: 0; height: 90px; }
  .envelope .brand { left: 46px; top: 32px; font-size: 21px; }
  .envelope .brand-dot { width: 11px; height: 11px; }
  .envelope-contact {
    position: absolute; left: 46px; top: 67px;
    font-size: 8px; line-height: 11px; color: var(--navy);
  }
  .address-window {
    position: absolute; left: 267px; top: 113px; width: 235px; height: 116px;
    background: var(--paper); border-radius: 10px;
  }
</style>
</head>
<body>

<section class="piece letterhead" aria-label="Letterhead">
  <svg class="band" viewBox="0 0 535 120" preserveAspectRatio="none" aria-hidden="true">
    <path d="M300,0 L535,0 L535,95 C470,70 400,30 300,0 Z" fill="var(--band-mid)"/>
    <path d="M0,110 L535,110" stroke="var(--band-light)" stroke-width="2"/>
  </svg>
  <div class="brand"><span class="brand-dot"></span>Vikmarka</div>
  <div class="letterhead-rule"></div>
  <div class="letterhead-footer">
    <p>Web: www.brekkafrakt.no &nbsp;|&nbsp; Email: Leif@brekkafrakt.no</p>
    <p>Telephone: 47382950 &nbsp;|&nbsp; Address: 8640 Brekka, Norway</p>
    <p>Org.nr: 983 517 608</p>
  </div>
</section>

<section class="piece business-card" aria-label="Business card">
  <svg class="band" viewBox="0 0 230 30" preserveAspectRatio="none" aria-hidden="true">
    <rect x="0" y="8" width="230" height="22" fill="var(--band-deep)"/>
    <rect x="0" y="2" width="230" height="2" fill="var(--band-light)"/>
  </svg>
  <div class="brand"><span class="brand-dot"></span>Vikmarka</div>
  <div class="card-details">
    <p class="card-name">Leif Dahlberg</p>
    <p>8640 Brekka</p>
    <p>47382950</p>
    <p>Leif@brekkafrakt.no</p>
    <p>www.brekkafrakt.no</p>
  </div>
</section>

<section class="piece sticker" aria-label="Sticker">
  <svg class="band" viewBox="0 0 184 14" preserveAspectRatio="none" aria-hidden="true">
    <rect x="0" y="2" width="184" height="6" fill="var(--band-deep)"/>
    <rect x="0" y="11" width="184" height="1.5" fill="var(--band-light)"/>
  </svg>
  <div class="brand"><span class="brand-dot"></span>Vikmarka</div>
  <div class="sticker-text">
    <p>Tekst and link:</p>
    <p class="accent">FRAKTÆ AV VIKMARKA.</p>
    <p class="accent">KE DU SYNS?</p>
    <p>Brekkafrakt.no/tilbakemelding</p>
    <p class="phone">Tel: 47382950</p>
  </div>
</section>

<section class="piece envelope" aria-label="Envelope">
  <svg class="band" viewBox="0 0 560 90" preserveAspectRatio="none" aria-hidden="true">
    <path d="M0,0 C60,50 150,70 260,72 L260,90 L0,90 Z" fill="var(--band-mid)"/>
    <rect x="0" y="84" width="560" height="6" fill="var(--band-deep)"/>
  </svg>
  <div class="brand"><span class="brand-dot"></span>Vikmarka</div>
  <div class="envelope-contact">
    <p>www.brekkafrakt.no |Leif@brekkafrakt.no</p>
    <p>47382950 |8640 Brekka, Norway</p>
    <p>Org.nr 983 517 608</p>
  </div>
  <div class="address-window"></div>
</section>

</body>
</html>
```